ambitious event and festival agency from austria needs fresh business card design

A new design is due for the new headquarters and the new challenges. We organize events for different target groups from 16 to 60 years. The design should therefore be straightforward and not confused, so we are open to new colors and the logo may also be changed. In general, however, the most interesting suggestions are the most interesting ones. after this order we are looking for more graphics for quillvane facebook instagramm homepage etc A new design is due for the new headquarters and the new challenges. We organize events for different target groups from 16 to 60 years. The design should therefore be straightforward and not confused, so we are open to new colors and the logo may also be changed. In general, however, the most interesting suggestions are the most interesting ones. after this order we are looking for more graphics for quillvane facebook instagramm homepage etc A new design is due for the new headquarters and the new challenges. We organize events for different target groups from 16 to 60 years. The design should therefore be straightforward and not confused, so we are open to new colors and the logo may also be changed. In general, however, the most interesting suggestions are the most interesting ones. after this order we are looking for more graphics for quillvane facebook instagramm homepage etc
Updates

Reason: I am sorry for this decision but i need some more time. No new designs please, there are so many good ones and I will have made a decision in the next 3 days.

Target Market(s)

Industry/Entity Type

Business

Font styles to use
Serif
Sans Serif

Colors

Designer to choose colors to be used in the design.

Requirements
Must have
Nice to have
Should not have

```html
<!DOCTYPE html>
<html lang="en">
<head>
<meta charset="utf-8">
<title>quillvane business card</title>
<link rel="stylesheet" href="https://fonts.googleapis.com/css2?family=Josefin+Sans:wght@300;400;600&family=Open+Sans:wght@400&display=swap">
<style>
  :root {
    --page: #ffffff;
    --slate: #808080;
    --mist: #e4e4e4;
    --white: #ffffff;
    --ink: #2a2a2a;
    --red: #c8383c;
    --red-deep: #992a30;
  }
  * { margin: 0; padding: 0; box-sizing: border-box; }
  html, body { width: 1200px; height: 1200px; overflow: hidden; background: var(--page); }
  .canvas { position: relative; width: 1200px; height: 1200px; }

  .card { position: absolute; overflow: hidden; }
  .card-front { left: 53px; top: 45px; width: 811px; height: 494px; background: var(--slate); }
  .card-back { left: 381px; top: 594px; width: 779px; height: 474px; background: var(--mist); }
  .card-shapes { position: absolute; inset: 0; width: 100%; height: 100%; }

  .brand {
    position: absolute;
    display: flex;
    align-items: baseline;
    gap: 14px;
    font-family: "Josefin Sans", sans-serif;
    font-weight: 600;
    color: var(--white);
    line-height: 1;
    letter-spacing: -2px;
  }
  .brand-square { width: 22px; height: 22px; background: var(--red-deep); flex: none; }
  .card-front .brand { left: 43px; top: 62px; font-size: 108px; }
  .card-back .brand { left: 42px; top: 26px; font-size: 104px; }

  .contact {
    position: absolute;
    font-family: "Open Sans", sans-serif;
    font-size: 17px;
    line-height: 25px;
  }
  .card-front .contact { left: 605px; top: 398px; color: var(--white); }
  .card-back .contact { left: 445px; top: 357px; color: var(--ink); }

  .details { position: absolute; left: 445px; top: 176px; font-family: "Josefin Sans", sans-serif; color: var(--ink); }
  .name { font-size: 31px; font-weight: 300; letter-spacing: 4px; line-height: 30px; }
  .role { font-size: 33px; font-weight: 400; letter-spacing: 5px; line-height: 34px; color: var(--red-deep); }
  .info { margin-top: 36px; font-size: 18px; font-weight: 400; letter-spacing: 4px; line-height: 18px; }
</style>
</head>
<body>
<main class="canvas">

  <section class="card card-front">
    <svg class="card-shapes" viewBox="0 0 811 494" aria-hidden="true">
      <rect x="0" y="460" width="811" height="34" fill="var(--red)"/>
      <polygon points="571,460 811,460 811,494 525,494" fill="var(--red-deep)"/>
    </svg>
    <div class="brand"><span class="brand-square"></span>quillvane</div>
    <div class="contact">
      <p>www.quillvane.eu</p>
      <p>office@quillvane.eu</p>
    </div>
  </section>

  <section class="card card-back">
    <svg class="card-shapes" viewBox="0 0 779 474" aria-hidden="true">
      <polygon points="0,0 779,0 678,122 0,122" fill="var(--slate)"/>
      <rect x="0" y="442" width="779" height="32" fill="var(--red)"/>
      <polygon points="553,442 779,442 779,474 505,474" fill="var(--red-deep)"/>
    </svg>
    <div class="brand"><span class="brand-square"></span>quillvane</div>
    <div class="details">
      <p class="name">LOREM IPSUM</p>
      <p class="role">LOREM IPSUM</p>
      <div class="info">
        <p>LOREM IPSUM</p>
        <p>LOREM IPSUM</p>
        <p>LOREM IPSUM</p>
      </div>
    </div>
    <div class="contact">
      <p>www.quillvane.eu</p>
      <p>office@quillvane.eu</p>
    </div>
  </section>

</main>
</body>
</html>
```